Halvorn - Refresh the look and feel of an existing website

We currently have an existing website www.halvornworldadvisory.example however it needs a more refreshed 'look and feel'. We are a professional consultancy that works with large corporate organisations and government. Our 'tag line' is A New Way of Thinking. We want the site to communicate "Innovation" and Leading Edge Thinking.

Target Market(s)

Corporate and Professional Clients - Organisation and Business Change

Industry/Entity Type

Management Consulting

Number of Pages Required

1 page

Font styles to use
Sans Serif

Requirements
Must have
• Must have a professional Corporate look and feel. Header 'imagery' is ok but boxes on front page need changing ... along with the words. The focus on home page needs to 'call out' 3 main consulting areas:-
• - Change & Transformation Specialists
• - Innovative Solutions
• - Digital Transformation
• Tag Line for business is ... A New Way of Thinking (Highlighting Halvorn as 'Thought Leaders' in business)
Nice to have
• Less "words' more imagery. Possibly an area for a 'video' or recent articles/blogs on the front page. Needs to have more of an 'interactive' feel. We are open to suggestions.
Should not have
• NA

```html
<!DOCTYPE html>
<html lang="en">
<head>
<meta charset="utf-8">
<title>Halvorn World Advisory</title>
<link rel="stylesheet" href="https://fonts.googleapis.com/css2?family=Oswald:wght@400;500&family=Raleway:wght@300;400;500&family=Open+Sans:wght@400;600&display=swap">
<style>
:root{
  --navy:#23395b;
  --navy-dark:#1b2d47;
  --ink:#3a3a3a;
  --muted:#555;
  --grey-line:#e4e4e4;
  --charcoal:#262626;
  --black:#0e0e0e;
  --field:#1d1d1d;
  --white:#fff;
  --footer:#080808;
}
*{margin:0;padding:0;box-sizing:border-box}
html,body{width:715px;height:1200px;overflow:hidden}
body{position:relative;background:var(--white);font-family:"Raleway",sans-serif;color:var(--ink)}
.abs{position:absolute}

/* hero */
.hero{left:0;top:0;width:715px;height:305px;overflow:hidden}
.hero-photo{position:absolute;inset:0;background:linear-gradient(100deg,#3b3a36 0%,#6b6557 22%,#8b8a82 45%,#a7a39a 62%,#c9c6be 80%,#b6b1a5 100%)}
.hero-shade{position:absolute;inset:0;background:rgba(0,0,0,.18)}
.hero-title{position:absolute;left:0;width:715px;top:126px;text-align:center;font-family:"Oswald",sans-serif;font-weight:400;font-size:43px;line-height:1;color:var(--white);font-variant:small-caps;letter-spacing:.3px}
.hero-sub{position:absolute;left:172px;width:371px;top:177px;text-align:center;font-family:"Open Sans",sans-serif;font-size:6.9px;line-height:7.6px;color:var(--white)}
.btn{position:absolute;top:197px;width:82px;height:17px;font-family:"Open Sans",sans-serif;font-size:7px;font-weight:600;color:var(--white);display:flex;align-items:center;justify-content:center;letter-spacing:.2px}
.btn-solid{left:265px;background:var(--navy);border:1px solid #8ba0bd}
.btn-ghost{left:353px;border:1px solid rgba(255,255,255,.7)}
.slide-arrow{position:absolute;top:137px;width:11px;height:32px;border:1px solid rgba(255,255,255,.6);display:flex;align-items:center;justify-content:center}
.slide-arrow.prev{left:0;border-left:none}
.slide-arrow.next{right:0;border-right:none}

/* nav */
.nav{left:107px;top:305px;width:487px;height:26px;border-bottom:1px solid #d8d8d8;box-shadow:0 2px 2px rgba(0,0,0,.06)}
.brand{position:absolute;left:30px;top:5px;display:flex;align-items:center;gap:4px;font-family:"Raleway",sans-serif;font-weight:500;font-size:10px;color:var(--navy);letter-spacing:.5px}
.brand-dot{width:16px;height:16px;border-radius:50%;background:var(--navy)}
.menu{position:absolute;right:1px;top:10px;display:flex;align-items:center;font-family:"Open Sans",sans-serif;font-size:6.4px;color:#666}
.menu span{display:flex;align-items:center}
.menu span+span::before{content:"";width:3px;height:3px;background:#c8c8c8;margin:0 5px}
.menu .active{color:var(--navy);font-weight:600}

/* services */
.section-title{left:0;width:715px;text-align:center;font-weight:400}
.services-title{top:342px;font-size:13px;color:#444}
.service{position:absolute;top:392px;width:155px;text-align:center}
.service svg{display:block;margin:0 auto}
.service h3{font-weight:400;font-size:9.6px;color:#444;margin-top:8px}
.service p{font-size:5.8px;line-height:8.4px;color:var(--muted);margin-top:7px}
.col-rule{position:absolute;width:1px;background:var(--grey-line)}

/* about */
.about{left:0;top:541px;width:399px;height:258px;background:var(--charcoal);color:var(--white)}
.about-photo{left:399px;top:541px;width:316px;height:258px;background:linear-gradient(120deg,#b9c7cf 0%,#8a9aa5 30%,#c4a088 55%,#5a6f92 75%,#a76a4a 100%)}
.about h2{position:absolute;left:108px;font-weight:400;font-size:12.5px;letter-spacing:.2px}
.about p{position:absolute;left:108px;width:284px;font-size:5.1px;line-height:7.5px}
.team{position:absolute;left:115px;top:158px;display:flex;gap:3px}
.member{width:55px;text-align:center;font-size:6.2px}
.member .portrait{width:55px;height:55px;margin-bottom:5px}

/* testimonials */
.testimonials{left:0;top:799px;width:715px;height:172px;background:linear-gradient(90deg,#e9e9e9,#f4f4f4 40%,#f7f7f7 60%,#e6e6e6)}
.testimonials h2{position:absolute;left:0;width:715px;top:19px;text-align:center;font-weight:400;font-size:12.5px;color:#333}
.testimonials p{position:absolute;left:150px;width:415px;text-align:center;font-size:5.1px;line-height:7.5px;color:#555}
.quote-photo{position:absolute;left:335px;top:98px;width:45px;height:53px;background:linear-gradient(160deg,#8a7a66,#c9b29a 50%,#5c4e40);border:1px solid #ccc}
.quote-name{position:absolute;left:0;width:715px;top:153px;text-align:center;font-size:6.8px;font-weight:500;color:var(--navy);text-decoration:underline}

/* contact */
.contact{left:0;top:971px;width:715px;height:213px;background:var(--black);color:var(--white)}
.contact h2{position:absolute;left:0;width:715px;top:11px;text-align:center;font-weight:400;font-size:12.5px;letter-spacing:.4px;color:#ddd}
.field{position:absolute;left:106px;width:238px;background:var(--field);font-family:"Open Sans",sans-serif;font-size:5.2px;color:#aaa;padding:5px 4px}
.submit{position:absolute;left:253px;top:185px;width:90px;height:16px;background:var(--navy);font-family:"Open Sans",sans-serif;font-size:6.8px;font-weight:600;display:flex;align-items:center;justify-content:center}
.info{position:absolute;left:357px;top:76px;width:230px;font-family:"Open Sans",sans-serif}
.info h3{font-weight:400;font-size:10px;color:#e8e8e8}
.info p{font-size:6px;line-height:8.4px;color:#aaa;margin-top:3px;padding-left:1px}
.info-line{display:flex;align-items:center;gap:7px;font-size:6.3px;color:#aaa;height:13px}
.info-line:first-of-type{margin-top:6px}
.social{display:flex;gap:2px;margin-top:8px;padding-left:2px}
.social span{width:17px;height:17px;background:var(--white)}
.social span.alt{background:var(--navy-dark)}
.footer{left:0;top:1184px;width:715px;height:16px;background:var(--footer);font-family:"Open Sans",sans-serif;font-size:5.2px;color:#999;text-align:center;line-height:16px}
</style>
</head>
<body>

<header class="abs hero">
  <div class="hero-photo" role="img" aria-label="Photo of a thoughtful businessman in a bright modern office"></div>
  <div class="hero-shade"></div>
  <h1 class="hero-title">A New Way of Thinking</h1>
  <p class="hero-sub">We help corporate and government organisations lead change with confidence. Discover how Halvorn's thought leadership and leading edge thinking can transform your business today.</p>
  <span class="btn btn-solid">GET STARTED</span>
  <span class="btn btn-ghost">LEARN MORE</span>
  <span class="slide-arrow prev"><svg width="6" height="10" viewBox="0 0 6 10"><path d="M5 1 1 5l4 4" fill="none" stroke="#fff" stroke-width="1"/></svg></span>
  <span class="slide-arrow next"><svg width="6" height="10" viewBox="0 0 6 10"><path d="M1 1l4 4-4 4" fill="none" stroke="#fff" stroke-width="1"/></svg></span>
</header>

<nav class="abs nav">
  <div class="brand"><span class="brand-dot"></span>HALVORN</div>
  <div class="menu">
    <span class="active">Home</span><span>About Us</span><span>Our Services</span><span>Solutions</span><span>What's Happening</span><span>Contact Us</span>
  </div>
</nav>

<h2 class="abs section-title services-title">Our Services</h2>

<div class="col-rule" style="left:267px;top:380px;height:145px"></div>
<div class="col-rule" style="left:435px;top:380px;height:145px"></div>

<div class="service" style="left:107px">
  <svg width="28" height="28" viewBox="0 0 28 28" fill="none" stroke="var(--navy)" stroke-width="1.6"><path d="M5 12a9 9 0 0 1 16-5"/><path d="M21 2v5h-5"/><path d="M23 16a9 9 0 0 1-16 5"/><path d="M7 26v-5h5"/><circle cx="14" cy="14" r="2.5" fill="var(--navy)"/></svg>
  <h3>Change &amp; Transformation Specialists</h3>
  <p>We partner with our clients to lead every aspect of organisational change and transformation, from strategy and design through to lasting implementation.</p>
</div>
<div class="service" style="left:274px">
  <svg width="28" height="28" viewBox="0 0 28 28" fill="none" stroke="var(--navy)" stroke-width="1.6"><path d="M14 3a7.5 7.5 0 0 0-4.5 13.5c.8.7 1 1.5 1 2.5h7c0-1 .2-1.8 1-2.5A7.5 7.5 0 0 0 14 3z"/><path d="M11 22h6M12 25h4"/></svg>
  <h3>Innovative Solutions</h3>
  <p>Using the latest thinking and our extensive experience, we design leading edge models and solutions that help our clients solve complex business challenges.</p>
</div>
<div class="service" style="left:440px">
  <svg width="28" height="28" viewBox="0 0 28 28" fill="none" stroke="var(--navy)" stroke-width="1.6"><rect x="3" y="4" width="22" height="15" rx="1"/><path d="M10 24h8M14 19v5"/><path d="M8 14l4-4 3 3 5-5" /></svg>
  <h3>Digital Transformation</h3>
  <p>We help organisations embrace digital ways of working, aligning people, process and technology to deliver sustainable outcomes for the 21st Century.</p>
</div>

<section class="abs about">
  <h2 style="top:36px">ABOUT US</h2>
  <p style="top:56px">The team at Halvorn World Advisory has wide ranging experience and is well-placed to support all aspects of our global community.All of our models and programs are leading edge and support a new way of thinking for the 21st Century.</p>
  <h2 style="top:86px">OUR TEAM</h2>
  <p style="top:111px">Our strength is our people - highly skilled, dedicated specialists who have proven experience delivering the outcomes that our clients want.&nbsp; Our people are your partners, and will 'roll up their sleeves' to deliver real results for your business.With a broad range of experience across business and community, our specialists are qualified and trained in all aspects of solution design and delivery.&nbsp; Our people have first-hand knowledge of the challenges inherent in transforming to meet future needs.</p>
  <div class="team">
    <div class="member"><div class="portrait" role="img" aria-label="Portrait of Jonathan Doe" style="background:linear-gradient(160deg,#6d6a66,#a59c92 50%,#2f2d2c)"></div>Jonathan Doe</div>
    <div class="member"><div class="portrait" role="img" aria-label="Portrait of Robert Doe" style="background:linear-gradient(160deg,#5e6064,#9a9995 50%,#3c4049)"></div>Robert Doe</div>
    <div class="member"><div class="portrait" role="img" aria-label="Portrait of Hannah Doe" style="background:linear-gradient(160deg,#7b6f60,#c8b49d 50%,#6a5a4a)"></div>Hannah Doe</div>
    <div class="member"><div class="portrait" role="img" aria-label="Portrait of Megan Doe" style="background:linear-gradient(160deg,#5a3a30,#c9826a 50%,#8a3d2c)"></div>Megan Doe</div>
  </div>
</section>
<div class="abs about-photo" role="img" aria-label="Photo of two colleagues smiling while reviewing notes at a café table"></div>

<section class="abs testimonials" aria-label="Testimonials">
  <h2>TESTIMONIALS</h2>
  <p style="top:45px">There are many variations of passages of Lorem Ipsum available, but the majority have suffered alteration in some form, by injected humour, or randomised words which don't look even slightly believable. If you are going to use a passage of Lorem Ipsum,</p>
  <p style="top:67px">Contrary to popular belief, Lorem Ipsum is not simply random text. It has roots in a piece of classical Latin literature from 45 BC, making it over 2000 years old. Edwin Marlowe, a Latin professor at Ashcombe College in Virginia, looked up one of the more obscure Latin words, consectetur, from a Lorem Ipsum passage,</p>
  <div class="quote-photo" role="img" aria-label="Portrait of testimonial author Megan Doe"></div>
  <div class="quote-name">Megan Doe</div>
</section>

<section class="abs contact">
  <h2>GET IN TOUCH</h2>
  <div class="field" style="top:43px;height:16px">Name:</div>
  <div class="field" style="top:62px;height:16px">Phone:</div>
  <div class="field" style="top:82px;height:16px">Email:</div>
  <div class="field" style="top:101px;height:82px">Comments:</div>
  <div class="submit">Submit</div>
  <div class="info">
    <h3>Contact Info</h3>
    <p>There are many variations of passages of Lorem Ipsum available, but the majority have suffered alteration in some form, by injected humour, or randomised words which don't look even slightly believable.</p>
    <div class="info-line"><svg width="7" height="9" viewBox="0 0 7 9"><path d="M3.5 9S0 5 0 3.5a3.5 3.5 0 0 1 7 0C7 5 3.5 9 3.5 9z" fill="#999"/><circle cx="3.5" cy="3.5" r="1.3" fill="#0e0e0e"/></svg>Address: 12b Harbour Row, Leeds, UK</div>
    <div class="info-line"><svg width="9" height="7" viewBox="0 0 9 7"><rect width="9" height="7" fill="#999"/><path d="M0 0l4.5 4L9 0" fill="none" stroke="#0e0e0e" stroke-width=".8"/></svg>Email: info@halvornworldadvisory.example</div>
    <div class="info-line"><svg width="8" height="8" viewBox="0 0 8 8"><path d="M1 0h2l1 2-1.2 1a4 4 0 0 0 2.2 2.2L6 4l2 1v2c0 .6-.4 1-1 1A7 7 0 0 1 0 1c0-.6.4-1 1-1z" fill="#999"/></svg>Call: 555-010-0199</div>
    <div class="social"><span aria-label="Social link"></span><span aria-label="Social link"></span><span class="alt" aria-label="Social link"></span><span aria-label="Social link"></span></div>
  </div>
</section>

<footer class="abs footer">© 2016 Halvorn World Advisory All Right Reserved</footer>

</body>
</html>
```